Emerging Australian photographer

I'm based in Cunderdin, a small rural town in the Wheatbelt area of Western Australia. So its a good thing that I love to travel further afield both for pleasure and for work. To me that is one and the same thing in any event!

My desire is to take photos that make the viewers heart skip. I love taking photos of people doing the things they love or being with the people they love. For me, the joy of photography comes with capturing the 'moments between the moments'. I like candid photography best of all - like when the new husband is staring joyfully at his bride and at that minute is unaware of the photographer capturing the moment.

I am available for weddings, engagements, birthdays, special events, newborns, family or individual portraits. By the end of the year I will be accredited with the Coastal Guild of Image Artisans.

I need a card that stands out but is elegant and would sit well on the table at a wedding or be given out in the church grounds. Classy and a little bit sassy.

Target Market(s)

Consumers who are seeking photographic services, eg wedding guests who see me at work and make enquiries.

Industry/Entity Type

Church

Contact Information for Business Card

Tamsin Bexley Photography
Tamsin Bexley
0452 307 618
www.tamsinbexley.com.au
photos@tamsinbexley.com.au

Requirements
Must have
• Must fit with the theme in the watermarks, but be crisp and modern.
Nice to have
• However it's not essential to have the pink! Facebook and Twitter logos.
Should not have
• Old style fonts like times new roman.

```html
<!DOCTYPE html>
<html lang="en">
<head>
<meta charset="utf-8">
<title>Tamsin Bexley Photography — Business Card</title>
<link rel="stylesheet" href="https://fonts.googleapis.com/css2?family=Arvo:wght@400;700&display=swap">
<style>
  :root {
    --backdrop: #e9e7e4;
    --card: #ffffff;
    --frame: #2a2a2a;
    --ink: #5f5f5f;
    --ink-strong: #4a4a4a;
    --accent: #eda3c4;
  }
  * { box-sizing: border-box; margin: 0; padding: 0; }
  html, body {
    width: 1200px;
    height: 904px;
    overflow: hidden;
    background: var(--backdrop);
  }
  .canvas {
    width: 1200px;
    height: 904px;
    display: flex;
    align-items: center;
    justify-content: center;
    gap: 60px;
  }
  .card {
    position: relative;
    width: 520px;
    height: 320px;
    background: var(--card);
    box-shadow: 0 6px 18px rgba(0,0,0,0.12);
  }
  .card__frame {
    position: absolute;
    inset: 0;
    width: 100%;
    height: 100%;
  }
  .card__content {
    position: absolute;
    inset: 0;
    display: flex;
    flex-direction: column;
    align-items: center;
    justify-content: center;
    font-family: "Arvo", serif;
    color: var(--ink);
  }
  .brand {
    display: flex;
    align-items: center;
    gap: 10px;
  }
  .brand__dot {
    width: 10px;
    height: 10px;
    border-radius: 50%;
    background: var(--accent);
  }
  .brand__name {
    font-size: 22px;
    font-weight: 400;
    color: var(--ink);
    letter-spacing: 0.5px;
  }
  .contact {
    align-items: flex-start;
    padding-left: 150px;
  }
  .contact__name {
    font-size: 17px;
    font-weight: 700;
    letter-spacing: 1.5px;
    text-transform: uppercase;
    color: var(--ink-strong);
    margin-bottom: 16px;
  }
  .contact__line {
    font-size: 15px;
    line-height: 1.55;
  }
  .social {
    display: flex;
    gap: 8px;
    margin-top: 10px;
  }
  .social__mark {
    width: 20px;
    height: 20px;
    border-radius: 50%;
    background: var(--accent);
  }
</style>
</head>
<body>
<main class="canvas">

  <section class="card card--front">
    <svg class="card__frame" viewBox="0 0 520 320" aria-hidden="true">
      <rect x="22" y="22" width="476" height="276" fill="none" stroke="var(--frame)" stroke-width="2"/>
      <rect x="29" y="29" width="462" height="262" fill="none" stroke="var(--frame)" stroke-width="0.8"/>
    </svg>
    <div class="card__content">
      <div class="brand">
        <span class="brand__dot"></span>
        <span class="brand__name">Tamsin Bexley Photography</span>
      </div>
    </div>
  </section>

  <section class="card card--back">
    <svg class="card__frame" viewBox="0 0 520 320" aria-hidden="true">
      <rect x="22" y="22" width="476" height="276" fill="none" stroke="var(--frame)" stroke-width="2"/>
      <rect x="29" y="29" width="462" height="262" fill="none" stroke="var(--frame)" stroke-width="0.8"/>
    </svg>
    <div class="card__content contact">
      <p class="contact__name">Tamsin Bexley</p>
      <p class="contact__line">www.tamsinbexley.com.au</p>
      <p class="contact__line">photos@tamsinbexley.com.au</p>
      <p class="contact__line">0452 307 618</p>
      <div class="social">
        <span class="social__mark"></span>
        <span class="social__mark"></span>
      </div>
    </div>
  </section>

</main>
</body>
</html>
```